Spa Business Card Design Project

Hello! We are a boutique spa for men and women that is rebranding. I would like a memorable new business card that showcases our beautiful new logo and our unique business. I would like it to be classic/timeless and eclectic/artistic at the  same time.
I am a fan of negative space as you can tell from the logo. I am also open to any creative ideas.
Multi sided design. Two sided design is acceptable as an option, too. "Flaps/folds/whatever the design term is" are optional- whether full vertical or horizontal, half flap, full flap etc
On either side next to the golden snail I would potentially like to see "slow down. Enjoy Life."  Possibly on one statment on top of each other, crowned with the snail. Or the statment following the snail on one line... I am open for a creative suprise, too.
The back I would like room for the standard Information
"3817 Birch Lane
Ashford, Vermont 05761
(518) 462 3085
info@thecorvella spa.com
The snail is to be done in gold ink.
Can I also Have an option for cards that are individualized for staff members, too?

Updates
Project Deadline Extended
Reason: I apologize for the deadline extension. My day was more involved than anticipated in other matters. Hope to have this closed by next Tuesday.
Thank you

Target Market(s)
Men and women with expendable income between the ages of 30-55
Industry/Entity Type
Boutique
Requirements
Must have
- only black and gold ink.

Nice to have
- One of a kind.
Showcase the snail :-)
make you smile :-)
Fun, but professional.
Should not have
- Lots of color.
Too feminine.
Too busy.

```html
<!DOCTYPE html>
<html lang="en">
<head>
<meta charset="utf-8">
<title>The Corvella Spa — Business Card</title>
<link rel="stylesheet" href="https://fonts.googleapis.com/css2?family=Didact+Gothic&family=Cedarville+Cursive&display=swap">
<style>
  :root {
    --paper: #ffffff;
    --stage: #ffffff;
    --ink: #231f20;
    --ink-soft: #555555;
    --gold: #c99a3c;
    --sand: #ecdfc6;
    --rule: #d8d8d8;
    --edge: #e4e4e4;
  }
  * { box-sizing: border-box; margin: 0; padding: 0; }
  html, body {
    width: 1200px; height: 900px; overflow: hidden;
    background: var(--stage);
    font-family: "Didact Gothic", "Century Gothic", sans-serif;
    color: var(--ink);
  }
  .canvas { position: relative; width: 1200px; height: 900px; }
  .card {
    position: absolute; left: 226px; width: 772px; height: 386px;
    background: var(--paper); overflow: hidden;
    border: 1px solid var(--edge);
  }
  .card--front { top: 44px; }
  .card--back { top: 466px; }

  .shell-area { position: absolute; background: var(--sand); }
  .card--front .shell-area {
    left: 486px; top: 46px; width: 310px; height: 280px;
    border-radius: 150px 150px 40px 40px;
  }
  .card--back .shell-area {
    left: -40px; top: 26px; width: 300px; height: 298px;
    border-radius: 150px 150px 30px 30px;
  }

  .brand {
    position: absolute; left: 54px; top: 46px; width: 420px;
    text-align: center;
  }
  .brand__name {
    font-size: 52px; line-height: 1; letter-spacing: 1px;
    color: var(--ink); text-transform: uppercase; font-weight: 400;
  }
  .brand__tagline { margin-top: 14px; font-size: 22px; color: var(--ink); }

  .staff {
    position: absolute; left: 144px; top: 262px; width: 240px; text-align: center;
  }
  .staff__name {
    font-family: "Cedarville Cursive", cursive;
    font-size: 24px; line-height: 1.3; color: var(--ink-soft);
    padding-bottom: 2px; border-bottom: 1px solid var(--rule);
  }
  .staff__role { margin-top: 4px; font-size: 17px; color: var(--ink); }

  .motto {
    position: absolute; left: 354px; top: 40px; width: 376px;
    border-bottom: 2px solid var(--gold); padding-bottom: 4px;
    display: flex; align-items: flex-end; justify-content: space-between;
  }
  .motto__text {
    font-family: "Cedarville Cursive", cursive;
    font-size: 26px; line-height: 1.3; color: var(--ink-soft); letter-spacing: 1px;
  }
  .motto__dot {
    width: 12px; height: 12px; border-radius: 50%; background: var(--gold);
    margin-bottom: 4px;
  }

  .contact {
    position: absolute; left: 354px; top: 162px;
    font-size: 21px; line-height: 30px; color: var(--ink);
    font-style: normal;
  }
  .contact__line--phone { margin-top: 16px; }
  .contact__line--email { margin-top: 22px; }
  .contact__label { color: var(--gold); margin-right: 6px; }
</style>
</head>
<body>
<main class="canvas">

  <section class="card card--front" aria-label="Card front">
    <div class="shell-area" role="img" aria-label="Large pale gold snail shell decoration"></div>
    <header class="brand">
      <h1 class="brand__name">The<br>Corvella<br>Spa</h1>
      <p class="brand__tagline">a quiet retreat for Men &amp; Women</p>
    </header>
    <div class="staff">
      <p class="staff__name">Clara Benning</p>
      <p class="staff__role">Therapist</p>
    </div>
  </section>

  <section class="card card--back" aria-label="Card back">
    <div class="shell-area" role="img" aria-label="Large pale gold snail shell decoration"></div>
    <div class="motto">
      <p class="motto__text">Take your time. Breathe.</p>
      <span class="motto__dot" aria-hidden="true"></span>
    </div>
    <address class="contact">
      <p class="contact__line">3817 Birch Lane</p>
      <p class="contact__line">Ashford, Vermont 05761</p>
      <p class="contact__line contact__line--phone"><span class="contact__label">P:</span>(518) 462 3085</p>
      <p class="contact__line contact__line--email"><span class="contact__label">E:</span>info@thecorvella spa.com</p>
    </address>
  </section>

</main>
</body>
</html>
```